Recruitment of Brindle Crew Staffing for the UK market

I want a website for the UK market to attract businesses and companies to come to us for Philipine labour. We want an information site that gives all information on what we do and how we can recruit Philippine labour.
This is a recruitment site for companies to contact us with their requirements for skilled workers coming from the Philipines over to the UK to work.

Target Market(s)

Uk Companies and businesses who want Philipine skilled workers

Industry/Entity Type

REcruitment

Coding

Coded - Design and coding required

Number of Pages Required

5+ page

Font styles to use
Sans Serif

Colors
0054AA
0677BA
7BADD7
CADEEF
E8F1F8
0094D4
00A9DD
6FCCEA
C7EBF8
E9F6FB
EE7325
F08F49
F5BC92
FAE3D3
FDF4ED
EB3D1F
EC4F4E
F09395
F8D3D4
FCEDEE

Requirements
Must have
• Look professional and corperate with drop down menus for Home ,about, services,articles. training , contact us
Nice to have
• Look at Tolvane recruitment- https://tolvanerecruitment.example.co.uk/. This is my current site - https://www.brindlecrewstaffing.example.com/
Should not have
• Cartoons or silly pictures , needs to be corperate looking

```html
<!DOCTYPE html>
<html lang="en">
<head>
<meta charset="utf-8">
<title>Brindle Crew Staffing – Recruiting Skilled Philippine Workers</title>
<link href="https://fonts.googleapis.com/css2?family=Roboto:wght@400;500;700&family=Roboto+Condensed:ital,wght@1,700&display=swap" rel="stylesheet">
<style>
:root{
  --red:#EB3D1F;
  --red-soft:#EC4F4E;
  --ink:#1d1d1f;
  --text:#555;
  --muted:#8a8a8a;
  --grey-bg:#f4f4f5;
  --line:#dcdcdc;
  --footer:#1f2024;
  --white:#fff;
}
*{margin:0;padding:0;box-sizing:border-box}
html,body{width:1200px;height:5038px;overflow:hidden}
body{font-family:"Roboto",sans-serif;color:var(--text);background:var(--white);position:relative}
.abs{position:absolute}
.heading{font-family:"Roboto Condensed",sans-serif;font-style:italic;font-weight:700;color:var(--ink)}
.heading em{color:var(--red);font-style:italic}
.eyebrow{font-size:13px;letter-spacing:6px;color:#666;text-transform:uppercase}
.rule{width:44px;height:2px;background:var(--red)}
.btn{display:inline-flex;align-items:center;gap:8px;border-radius:24px;color:#fff;font-weight:500;font-size:14px}
.btn svg{width:18px;height:10px}

/* header */
.site-header{top:0;left:0;width:1200px;height:88px;background:#fff;box-shadow:0 1px 6px rgba(0,0,0,.06)}
.brand{left:52px;top:24px;font-size:30px;font-weight:700;color:#8e1b1b;display:flex;align-items:center;gap:10px}
.brand .dot{width:14px;height:14px;background:var(--red)}
.nav{left:381px;top:36px;display:flex;gap:30px;font-size:13px;color:#444;text-transform:uppercase}
.nav .active{color:var(--red)}
.phone-band{left:905px;top:0;width:295px;height:88px;background:var(--red);clip-path:polygon(40px 0,100% 0,100% 100%,0 100%);display:flex;align-items:center;padding-left:52px;gap:10px;color:#fff;font-size:25px;font-weight:700}

/* hero */
.hero{top:88px;left:0;width:1200px;height:577px;background:linear-gradient(100deg,#3a2c24 0%,#6b5445 45%,#8c7462 70%,#4a3b33 100%)}
.hero-title{left:137px;top:200px;border-left:4px solid #fff;padding-left:0;font-size:40px;line-height:46px;color:#fff}
.hero-title span{display:block;padding-left:4px}
.hero-title .red{color:var(--red)}
.hero-sub{left:124px;top:345px;font-size:15px;line-height:25px;color:#fff;width:440px}
.hero .btn{left:124px;top:416px;height:44px;padding:0 26px;background:var(--red);text-transform:uppercase}
.contact-card{left:739px;top:84px;width:336px;height:410px;background:#fff;border-top:4px solid var(--red);padding:22px 30px}
.contact-card h2{font-size:28px;text-align:center;margin-bottom:18px}
.field{height:40px;border:1px solid var(--line);border-radius:3px;margin-bottom:12px;display:flex;align-items:center;gap:8px;padding-left:12px;font-size:12px;color:#999;font-style:italic}
.field.tall{height:78px;align-items:flex-start;padding-top:10px}
.field svg{width:12px;height:12px;fill:#bbb}
.contact-card .btn{margin-top:2px;height:44px;padding:0 24px;background:#1b1b1b}

/* about */
.photo{background:linear-gradient(135deg,#c9ccd2,#8d97a6)}
.about-text{left:660px;top:775px;width:378px}
.about-text h2{font-size:34px;margin:10px 0 14px}
.about-text p{font-size:12.5px;line-height:23px;margin-top:16px}
.about-text .btn{margin-top:24px;height:40px;padding:0 24px;background:var(--red)}

/* recruit */
.band-grey{left:0;width:1200px;background:var(--grey-bg)}
.section-head{left:0;width:1200px;text-align:center}
.section-head h2{font-size:34px;margin-top:10px}
.section-head .rule{margin:12px auto 0}
.section-head p{margin-top:22px;font-size:15px;color:#333}
.step{width:400px}
.step-title{display:flex;align-items:center;gap:14px}
.step-num{width:40px;height:40px;border-radius:50%;background:var(--red);color:#fff;font-weight:700;font-size:20px;display:flex;align-items:center;justify-content:center}
.step-title h3{font-size:28px}
.step p{margin:16px 0 0 56px;font-size:12.5px;line-height:23px}
.frame::before{content:"";position:absolute;top:-8px;right:-8px;width:210px;height:170px;border-top:6px solid var(--red);border-right:6px solid var(--red)}
.frame.left::before{right:auto;left:-8px;border-right:0;border-left:6px solid var(--red)}

/* cards */
.card{width:278px;height:328px;background:#fff;box-shadow:0 2px 10px rgba(0,0,0,.06)}
.card-head{display:flex;gap:14px;align-items:flex-end}
.card-icon{width:86px;height:86px;background:var(--red);display:flex;align-items:center;justify-content:center}
.card-icon svg{width:46px;height:46px;stroke:#fff;fill:none;stroke-width:2}
.card-head h3{font-size:27px;line-height:30px;margin-bottom:4px}
.card-body{padding:22px 24px 0;font-size:12px;line-height:22px}
.card-body a{display:block;margin-top:12px;color:var(--red);font-weight:500;text-decoration:none}

/* footer */
.site-footer{top:4672px;left:0;width:1200px;height:366px;background:linear-gradient(180deg,#2a2b30,var(--footer))}
.footer-brand{left:165px;top:110px;font-size:30px;font-weight:700;color:#fff;display:flex;align-items:center;gap:10px}
.footer-brand .dot{width:14px;height:14px;background:var(--red)}
.socials{left:220px;top:186px;display:flex;gap:11px}
.socials span{width:34px;height:34px;border-radius:50%;border:2px solid #fff}
.socials span:first-child{background:var(--red);border-color:var(--red)}
.footer-col h4{color:#fff;font-size:17px;font-weight:700;margin-bottom:20px}
.footer-col li{list-style:none;color:#ccc;font-size:13px;line-height:27px}
.footer-col li.active{color:var(--red)}
.detail{display:flex;gap:12px;color:#ddd;font-size:12.5px;line-height:19px;margin-bottom:14px}
.detail svg{flex:none;width:14px;height:14px;fill:var(--red);margin-top:2px}
.detail b{color:#fff;font-weight:700}
.copyright{left:0;top:4990px;width:1200px;text-align:center;color:#ccc;font-size:13px;border-top:1px solid #3a3b40;padding-top:12px}
</style>
</head>
<body>

<header class="site-header abs">
  <div class="brand abs"><span class="dot"></span>Brindle Crew</div>
  <nav class="nav abs">
    <span class="active">Home</span><span>About</span><span>Services ▾</span><span>Articles</span><span>Training</span><span>Contact Us</span>
  </nav>
  <div class="phone-band abs">
    <svg width="26" height="26" viewBox="0 0 24 24" fill="#fff"><path d="M6.6 10.8a15 15 0 0 0 6.6 6.6l2.2-2.2c.3-.3.7-.4 1-.2 1.1.4 2.3.6 3.6.6.6 0 1 .4 1 1V20c0 .6-.4 1-1 1A17 17 0 0 1 3 4c0-.6.4-1 1-1h3.5c.6 0 1 .4 1 1 0 1.3.2 2.5.6 3.6.1.3 0 .7-.2 1z"/></svg>
    079 4410 2236
  </div>
</header>

<section class="hero abs" role="img" aria-label="Recruitment consultants meeting business clients around an office table">
  <h1 class="hero-title heading abs"><span>Recruiting And Placing</span><span class="red">Skilled Philippine Workers</span><span>Into UK Companies</span></h1>
  <p class="hero-sub abs">We source skilled workers directly from the Philippines to work in the UK.</p>
  <a class="btn abs">Contact Us <svg viewBox="0 0 18 10" fill="none" stroke="#fff" stroke-width="1.6"><path d="M0 5h16M12 1l4 4-4 4"/></svg></a>
  <form class="contact-card abs">
    <h2 class="heading">Contact Us Today</h2>
    <div class="field"><svg viewBox="0 0 12 12"><circle cx="6" cy="3.5" r="3"/><path d="M0 12a6 5 0 0 1 12 0z"/></svg>Name</div>
    <div class="field"><svg viewBox="0 0 12 12"><rect y="2" width="12" height="8"/></svg>Email</div>
    <div class="field"><svg viewBox="0 0 12 12"><rect x="3" width="6" height="12" rx="1"/></svg>Phone</div>
    <div class="field tall"><svg viewBox="0 0 12 12"><path d="M0 12l1-4 7-7 3 3-7 7z"/></svg>Message</div>
    <span class="btn">Send Message <svg viewBox="0 0 18 10" fill="none" stroke="#fff" stroke-width="1.6"><path d="M0 5h16M12 1l4 4-4 4"/></svg></span>
  </form>
</section>

<div class="photo abs" style="left:160px;top:788px;width:225px;height:245px" role="img" aria-label="Construction engineers in hard hats"></div>
<div class="photo abs" style="left:405px;top:758px;width:192px;height:195px;background:linear-gradient(135deg,#9fb6cf,#5d7a9a)" role="img" aria-label="Group of nurses in blue uniforms"></div>
<div class="photo abs" style="left:336px;top:973px;width:182px;height:180px;background:linear-gradient(135deg,#8a8f94,#4f5458)" role="img" aria-label="Workers in white hard hats on site"></div>
<div class="photo abs" style="left:176px;top:1050px;width:143px;height:142px;background:linear-gradient(135deg,#e6ecf2,#a9b8c7)" role="img" aria-label="Medical team in white coats"></div>

<div class="about-text abs">
  <div class="eyebrow">About</div>
  <h2 class="heading">Brindle Crew <em>Staffing</em></h2>
  <div class="rule"></div>
  <p>We source skilled workers directly from the Philippines to work in the UK. With offices, training locations and specialist recruiters we can find the highest quality individuals to add value and resources to any UK business. We delivery quality based on vast experience over a number of years.</p>
  <p>Our company has been established in the Philippines for <b>over 20 years.</b> We have mainly been recruiting philippine workers for the off shore industry in asia but since brexit and the new rules on skilled workers entering the UK we have been working with UK companies.</p>
  <span class="btn">Read More <svg viewBox="0 0 18 10" fill="none" stroke="#fff" stroke-width="1.6"><path d="M0 5h16M12 1l4 4-4 4"/></svg></span>
</div>

<div class="band-grey abs" style="top:1280px;height:2111px"></div>
<div class="section-head abs" style="top:1352px">
  <div class="eyebrow">Working Together</div>
  <h2 class="heading">Brindle Crew <em>Recruit</em></h2>
  <div class="rule"></div>
  <p>We recruit the finest talent available with our dedicated 200 strong team.</p>
</div>

<div class="step abs" style="left:160px;top:1573px">
  <div class="step-title"><span class="step-num">1</span><h3 class="heading">What We Do</h3></div>
  <p>Our company has been estiblished in the Philippines for <b>over 20 years.</b> We have mainly been recruiting philippine workers for the off shore industry in asia but since brexit and the new rules on skilled workers entering the UK we have been working with UK companies who now have chance to recruit some of the finest hard working talent from the Philippines for their companies.</p>
</div>
<div class="frame abs" style="left:610px;top:1519px;width:422px;height:342px"><div class="photo" style="width:100%;height:100%;background:linear-gradient(135deg,#d8dde2,#9a7a6a)" role="img" aria-label="Business professional selecting candidate profiles on a digital network"></div></div>

<div class="frame left abs" style="left:168px;top:1984px;width:418px;height:346px"><div class="photo" style="width:100%;height:100%;background:linear-gradient(135deg,#cfd6c8,#8ea39a)" role="img" aria-label="Passport visa page with an approved work permit stamp"></div></div>
<div class="step abs" style="left:639px;top:2046px">
  <div class="step-title"><span class="step-num">2</span><h3 class="heading">How We Help</h3></div>
  <p>We work with companies to find skilled workers that meet the UK requirements for Visas and work permits. We guide you through the whole process and deliver highly trained people that add value to your business. We are here to help both the companies and the Philippino people to gain a better standard of living for their families.</p>
</div>

<div class="step abs" style="left:160px;top:2511px">
  <div class="step-title"><span class="step-num">3</span><h3 class="heading">Where To Start</h3></div>
  <p>We need to know what your issues are and how we can understand the personnal you require , over what time frame and the number of employees you need. Once this is established we start sourcing workers in the Philippines that meet your criteria while starting the process in the UK to be able to have all the documents in place to deliver your company hard working skilled individuals.</p>
</div>
<div class="frame abs" style="left:610px;top:2457px;width:420px;height:343px"><div class="photo" style="width:100%;height:100%;background:linear-gradient(135deg,#b9c4cf,#5f6e7e)" role="img" aria-label="Two businessmen reviewing a contract together"></div></div>

<div class="frame left abs" style="left:168px;top:2922px;width:420px;height:346px"><div class="photo" style="width:100%;height:100%;background:linear-gradient(135deg,#e3e7ea,#7d8792)" role="img" aria-label="Smiling businessman shaking hands across a desk"></div></div>
<div class="step abs" style="left:639px;top:2985px">
  <div class="step-title"><span class="step-num">4</span><h3 class="heading">Contact Us Today</h3></div>
  <p>Please contact us today with your requirements , this can be care workers ,chef, welders, pipe fitters, caravan cabinet makers, medical workers. The UK list of required skills is extensive and the Philippines offerenglish speaking highly qualified hard working employees. Contact us today and make that first step to a highly motivated , quality skilled workforce.</p>
</div>

<div class="section-head abs" style="top:3460px">
  <div class="eyebrow">Centers</div>
  <h2 class="heading">Brindle Crew <em>Centers</em></h2>
  <div class="rule"></div>
  <p>Our centres are highlighted in red dots on the map.</p>
</div>
<div class="abs" style="left:450px;top:3613px;width:293px;height:463px;background:radial-gradient(ellipse at center,#e6e7e9 0%,#f3f3f4 60%,#fff 100%)" role="img" aria-label="Map of the Philippines with red markers at Baguio, Manila, Batangas, Bacolod and Davao"></div>

<div class="band-grey abs" style="top:4164px;height:508px"></div>

<article class="card abs" style="left:160px;top:4256px">
  <div class="card-head"><div class="card-icon"><svg viewBox="0 0 46 46"><rect x="8" y="6" width="24" height="32"/><path d="M14 14h12M14 20h12M14 26h8"/><circle cx="34" cy="32" r="6"/></svg></div><h3 class="heading">UK Skilled<br>Workers List</h3></div>
  <div class="card-body">The UK government since brexit have developed a new system based on points (similar to Australia) when recruiting from outside of the UK. Previously EU citizens could work in the UK without any extensive documentation or clarification...<a>Read More →</a></div>
</article>
<article class="card abs" style="left:461px;top:4256px">
  <div class="card-head"><div class="card-icon"><svg viewBox="0 0 46 46"><rect x="10" y="6" width="26" height="34"/><path d="M16 16h14M16 22h14M16 28h10"/><circle cx="16" cy="10" r="2"/></svg></div><h3 class="heading">Sponsor<br>Licence</h3></div>
  <div class="card-body">If you have areas of your business that meet the entry requirements of skilled labour your next step is to gain a sponsor licence for your business. There are different types of licences depending on the size of the business.<a>Read More →</a></div>
</article>
<article class="card abs" style="left:760px;top:4256px">
  <div class="card-head"><div class="card-icon"><svg viewBox="0 0 46 46"><circle cx="23" cy="14" r="6"/><path d="M10 40a13 13 0 0 1 26 0z"/><circle cx="34" cy="30" r="6"/></svg></div><h3 class="heading">Recruitment<br>Timeline</h3></div>
  <div class="card-body">Brief us on the job profiles – this is passed on to our teams in the Philippines.<br><span style="color:var(--red)">•</span> Our teams in the Philippines source suitable candidates, documentation required for each candidate will be checked and vetted by the...<a>Read More →</a></div>
</article>

<footer class="site-footer abs">
  <div class="footer-brand abs"><span class="dot"></span>Brindle Crew</div>
  <div class="socials abs"><span></span><span></span><span></span><span></span></div>
  <div class="footer-col abs" style="left:556px;top:80px">
    <h4>Quick Links</h4>
    <ul><li class="active">Home</li><li>About</li><li>Services</li><li>Articles</li><li>Training</li><li>Contact Us</li></ul>
  </div>
  <div class="footer-col abs" style="left:755px;top:80px;width:300px">
    <h4>Contact Details</h4>
    <div class="detail"><svg viewBox="0 0 14 14"><path d="M7 0a5 5 0 0 1 5 5c0 4-5 9-5 9S2 9 2 5a5 5 0 0 1 5-5z"/></svg><div><b>BRINDLE CREW STAFFING</b><br>Larkspur Court, Easthaven<br>EH00 4QT United Kingdom</div></div>
    <div class="detail"><svg viewBox="0 0 24 24"><path d="M6.6 10.8a15 15 0 0 0 6.6 6.6l2.2-2.2c.3-.3.7-.4 1-.2 1.1.4 2.3.6 3.6.6.6 0 1 .4 1 1V20c0 .6-.4 1-1 1A17 17 0 0 1 3 4c0-.6.4-1 1-1h3.5c.6 0 1 .4 1 1 0 1.3.2 2.5.6 3.6.1.3 0 .7-.2 1z"/></svg><b>079 4410 2236</b></div>
    <div class="detail"><svg viewBox="0 0 14 14"><rect y="2" width="14" height="10"/></svg>sales@brindlecrewstaffing.example.com</div>
  </div>
</footer>
<div class="copyright abs">© 2023 Brindle Crew Staffing Ltd. All Rights Reserved.</div>

</body>
</html>
```